Harbourgate Sydney CBD Corporate Squash League (est.1952)

The Sydney CBD Office Racquet Circuit began in 1952 and has been played every year since. It is the longest running continuous sporting competition in the Sydney CBD. It is a team squash competition from May to Oct yearly played between companies, sporting groups or just a groups of friends.
We are looking for a flyer that we can reuse every year (so the content within the flyer can't be tied to a specific time). Other specific we are looking for are
1. Squash imagery (can either be real or graphic design) depicting action / athleticism / friendly rivalry
2. Needs the following content
a ) "A Sydney CBD based competition for friendly rivalry between companies, sporting clubs or between friends"
b) "All matches in and around the CBD from 5.30pm to 8pm"
c) "We cater for all playing abilities"
d) "Ladies beginner comp includes complimentary coaching"
e) "Visit our website www.vkpla.org.au for more info or contact Martin on wolstenm@trl.com.au"

Flyer needs to include the logos attached in file upload section

```html
<!DOCTYPE html>
<html lang="en">
<head>
<meta charset="utf-8">
<title>Harbourgate Sydney CBD Corporate Squash League</title>
<link href="https://fonts.googleapis.com/css2?family=Montserrat:ital,wght@0,300;0,400;0,600;0,700;0,800;1,400;1,700;1,800&family=Russo+One&family=Bebas+Neue&display=swap" rel="stylesheet">
<style>
  :root{
    --navy:#1e3366;
    --navy-deep:#16284f;
    --yellow:#f8bd16;
    --yellow-soft:#fbd25a;
    --white:#ffffff;
    --silver-top:#ffffff;
    --silver-bottom:#8e96a3;
    --stage:#f1f1f1;
    --ink:#1b1b1b;
    --gold:#c9a24a;
  }
  *{margin:0;padding:0;box-sizing:border-box}
  html,body{width:1200px;height:3073px;overflow:hidden;background:var(--stage)}
  .flyer{position:absolute;left:50px;top:759px;width:1100px;height:1555px;overflow:hidden;background:var(--yellow);font-family:"Montserrat",sans-serif}
  .backdrop{position:absolute;inset:0}
  .masthead{position:absolute;left:0;right:0;text-align:center;color:var(--white)}
  .masthead__presenter{top:58px;font-weight:400;font-size:46px;letter-spacing:9px}
  .masthead__line{top:128px;font-family:"Russo One",sans-serif;font-style:italic;font-size:70px;letter-spacing:2px;transform:skewX(-8deg)}
  .masthead__league{top:196px;font-family:"Bebas Neue",sans-serif;font-size:138px;letter-spacing:6px;line-height:1;
    background:linear-gradient(180deg,var(--silver-top) 20%,var(--silver-bottom) 95%);-webkit-background-clip:text;background-clip:text;color:transparent}
  .masthead__est{top:318px;font-family:"Russo One",sans-serif;font-size:74px;transform:skewX(-10deg)}
  .player{position:absolute;border-radius:40px 40px 0 0}
  .player--left{left:0;top:330px;width:290px;height:546px;background:linear-gradient(180deg,#e9ddd2 0%,#f3f3f3 30%,#2a3a66 62%,#d9b79e 100%)}
  .player--right{left:830px;top:370px;width:270px;height:506px;background:linear-gradient(180deg,#5a3c2c 0%,#f2f0ea 30%,#efeae0 70%,#5a3c2c 100%)}
  .club-mark{position:absolute;left:50%;top:600px;transform:translateX(-50%);display:flex;align-items:center;gap:16px;color:var(--navy);font-family:"Montserrat",sans-serif;font-weight:800;font-size:44px;white-space:nowrap}
  .club-mark__dot{width:40px;height:40px;border-radius:50%;background:var(--navy)}
  .rivalry{position:absolute;left:0;right:0;top:886px;height:110px;background:var(--navy);text-align:center}
  .rivalry__lead{padding-top:14px;color:var(--yellow);font-weight:700;font-size:27px;letter-spacing:1px}
  .rivalry__main{font-family:"Bebas Neue",sans-serif;color:var(--white);font-size:58px;line-height:1;letter-spacing:1px}
  .based{position:absolute;left:0;right:0;top:1012px;text-align:center;color:var(--navy);font-weight:800;font-size:56px;line-height:1;letter-spacing:2px}
  .times{position:absolute;left:107px;top:1128px;width:886px;height:118px}
  .times svg{position:absolute;inset:0}
  .times__text{position:relative;text-align:center;font-style:italic}
  .times__lead{padding-top:10px;color:var(--white);font-weight:700;font-size:32px;letter-spacing:1px}
  .times__hours{color:var(--yellow);font-weight:800;font-size:58px;line-height:1;letter-spacing:1px}
  .note{position:absolute;left:0;right:0;height:42px;text-align:center;color:var(--ink);font-weight:700;font-size:29px;line-height:42px;
    background:linear-gradient(90deg,rgba(255,255,255,0) 0%,rgba(255,240,190,.95) 30%,rgba(255,240,190,.95) 70%,rgba(255,255,255,0) 100%)}
  .note--abilities{top:1258px}
  .note--ladies{top:1305px}
  .contact{position:absolute;left:0;right:0;top:1360px;height:93px;background:var(--navy);color:var(--white)}
  .contact__divider{position:absolute;left:400px;top:0;height:93px}
  .contact__block{position:absolute;font-style:italic;font-size:29px;line-height:1.15}
  .contact__block--web{left:70px;top:10px}
  .contact__block--mail{left:470px;top:6px}
  .contact__value{color:var(--yellow);font-weight:700;display:flex;align-items:center;gap:8px;font-size:30px}
  .sponsors{position:absolute;left:0;right:0;top:1459px;height:96px;background:var(--white)}
  .sponsors__tag{position:absolute;left:0;top:18px;width:390px;height:50px}
  .sponsors__tag-text{position:absolute;left:60px;top:22px;color:var(--yellow);font-weight:800;font-style:italic;font-size:34px;letter-spacing:1px}
  .sponsor{position:absolute;top:34px;display:flex;align-items:center;gap:8px;color:var(--navy);font-weight:600;font-size:13px;white-space:nowrap}
  .sponsor__mark{width:24px;height:24px;border-radius:50%;background:var(--navy)}
  .sponsor--association{left:410px}
  .sponsor--academy{left:740px}
  .sponsor__badge{position:absolute;left:1000px;top:16px;width:64px;height:64px;border-radius:50%;background:var(--navy);border:4px solid var(--gold)}
</style>
</head>
<body>
<main class="flyer">
  <svg class="backdrop" width="1100" height="1555" viewBox="0 0 1100 1555" aria-hidden="true">
    <defs>
      <radialGradient id="glow" cx="50%" cy="45%" r="50%">
        <stop offset="0" stop-color="#fde79a"/>
        <stop offset="1" stop-color="#f8bd16"/>
      </radialGradient>
    </defs>
    <rect width="1100" height="1555" fill="url(#glow)"/>
    <polygon points="0,0 1100,0 1100,335 550,560 0,355" fill="#1e3366"/>
    <polygon points="0,355 550,560 0,410" fill="#ffffff"/>
    <polygon points="1100,335 550,560 1100,395" fill="#ffffff"/>
    <polygon points="0,410 550,560 0,440" fill="#f8bd16"/>
  </svg>

  <p class="masthead masthead__presenter">HARBOURGATE SYDNEY</p>
  <h1 class="masthead masthead__line">CBD CORPORATE</h1>
  <p class="masthead masthead__league">SQUASH LEAGUE</p>
  <p class="masthead masthead__est">(EST.1952)</p>

  <div class="player player--left" role="img" aria-label="Photo of a female squash player lunging forward with her racquet"></div>
  <div class="player player--right" role="img" aria-label="Photo of a male squash player in white stretching into a shot"></div>

  <div class="club-mark"><span class="club-mark__dot"></span>Harbourline Squash</div>

  <section class="rivalry">
    <p class="rivalry__lead">FOR FRIENDLY RIVALRY BETWEEN COMPANIES,</p>
    <p class="rivalry__main">SPORTING CLUBS OR BETWEEN FRIENDS</p>
  </section>

  <h2 class="based">A SYDNEY CBD BASED<br>COMPETITION</h2>

  <section class="times">
    <svg width="886" height="118" viewBox="0 0 886 118" aria-hidden="true">
      <polygon points="0,0 886,0 856,118 30,118" fill="#ffffff"/>
      <polygon points="6,5 880,5 851,113 35,113" fill="#1e3366"/>
    </svg>
    <div class="times__text">
      <p class="times__lead">ALL MATCHES IN AND AROUND THE CBD FROM</p>
      <p class="times__hours">5.30PM TO 8PM</p>
    </div>
  </section>

  <p class="note note--abilities">We cater for all playing abilities</p>
  <p class="note note--ladies">Ladies beginner comp includes complimentary coaching</p>

  <section class="contact">
    <svg class="contact__divider" width="40" height="93" viewBox="0 0 40 93" aria-hidden="true">
      <line x1="34" y1="0" x2="6" y2="93" stroke="#ffffff" stroke-width="5"/>
    </svg>
    <div class="contact__block contact__block--web">
      <p>Visit our website</p>
      <p class="contact__value">
        <svg width="24" height="24" viewBox="0 0 24 24" aria-hidden="true"><circle cx="12" cy="12" r="10" fill="none" stroke="#fff" stroke-width="2"/><ellipse cx="12" cy="12" rx="4" ry="10" fill="none" stroke="#fff" stroke-width="2"/><line x1="2" y1="12" x2="22" y2="12" stroke="#fff" stroke-width="2"/></svg>
        www.vkpla.org.au
      </p>
    </div>
    <div class="contact__block contact__block--mail">
      <p>for more info or contact Martin on</p>
      <p class="contact__value">
        <svg width="24" height="18" viewBox="0 0 24 18" aria-hidden="true"><rect x="1" y="1" width="22" height="16" fill="#fff"/><polyline points="1,1 12,10 23,1" fill="none" stroke="#1e3366" stroke-width="2"/></svg>
        wolstenm@trl.com.au
      </p>
    </div>
  </section>

  <section class="sponsors">
    <svg class="sponsors__tag" width="390" height="50" viewBox="0 0 390 50" aria-hidden="true">
      <polygon points="0,0 390,0 372,50 0,50" fill="#1e3366"/>
    </svg>
    <p class="sponsors__tag-text">SPONSORED BY</p>
    <div class="sponsor sponsor--association"><span class="sponsor__mark"></span>NORTHGATE RACQUETS ASSOCIATION</div>
    <div class="sponsor sponsor--academy"><span class="sponsor__mark"></span>BAYSIDE SQUASH SCHOOL</div>
    <div class="sponsor__badge" aria-hidden="true"></div>
  </section>
</main>
</body>
</html>
```